Web Site for Strategy and Technology Consulting Company

We are looking for a website design that engages potential customers to understand our services and contact us. In this contest, we are looking for a homepage design, but the winning designer will be favored for the design of some of the more complicated interior pages of the site. An additional contest (or contests) for these pages will be added soon.

PLATROM AND RESPONSIVE DESIGN
The site will be implemented in WordPress using the Elementor page builder.
We are looking for a design that will look good on phones are well as laptop browsers.

UPLOADED FILES INCLUDE:
1a A wireframe of the homepage we are looking for. The Uploaded PDF also includes a draft of the text proposed for the homepage. Designers are free to go beyond the wireframe, but all elements of the wireframe should be included.
1b A Word document with the draft text of the homepage.
2a-d The Norvalith logo. Two versions are included – a dark version which works well against a light background, and a light version which works well against a dark background.
3 The Norvalith color palette with HEX and RGB values. Designers are not limited to this palette, but colors should be complementary.
4 A draft of the homepage menu
5 Service sheets with information on the services we provide

MORE ABOUT NORVALITH
Norvalith is a consulting company focused on transforming businesses through software. Our tagline, “Transformation Delivered,” recognizes the gap business often have between business transformation and the software they end up with. By listening to our customers and understanding their vision and where they are, we help get our customers where they want to go.

We increase our capability by working with many consultants and partners, allowing us to provide our customers with the best people and the software that best suits them.

Industry/Entity Type

Consulting

Number of Pages Required

1 page

Font styles to use
Sans Serif

Requirements
Must have
• the content represented on the wireframe uploaded
Nice to have
• interactive features, such as roll-over icons that reveal additional information

```html
<!DOCTYPE html>
<html lang="en">
<head>
<meta charset="utf-8">
<title>Norvalith — Transformation Delivered</title>
<link rel="stylesheet" href="https://fonts.googleapis.com/css2?family=Roboto+Condensed:wght@400;700&family=Montserrat:wght@400;500;600;700&family=Roboto:wght@400;500;700&display=swap">
<style>
:root{
  --blue:#245f96;
  --blue-dark:#1d4f7f;
  --yellow:#e8c53a;
  --sky:#a9cdea;
  --ink:#1b1b1b;
  --text:#333;
  --muted:#666;
  --line:#dedede;
  --card:#f8f8f8;
  --band:#f3f4f6;
  --footer:#2b2b2b;
}
*{margin:0;padding:0;box-sizing:border-box}
html,body{width:1200px;height:3769px;overflow:hidden;background:#fff}
body{position:relative;font-family:"Roboto",Arial,sans-serif;color:var(--text)}
.abs{position:absolute}
.heading{font-family:"Roboto Condensed",Arial,sans-serif;font-weight:700;color:var(--ink);line-height:1.05}
.heading .accent{color:var(--blue)}
.btn{position:absolute;display:flex;align-items:center;justify-content:center;background:var(--blue);color:#fff;font-family:"Roboto",sans-serif;font-weight:500;font-size:14px}
.sq{position:absolute}

/* header */
.site-header{position:absolute;left:0;top:0;width:1200px;height:86px;background:#fff}
.brand{position:absolute;left:110px;top:18px;font-family:"Roboto",sans-serif;font-weight:400;font-size:46px;color:#555;letter-spacing:-1px}
.nav-item{position:absolute;top:36px;font-size:13px;color:#222}
.nav-item::after{content:"";display:inline-block;width:5px;height:5px;border-right:1.5px solid #222;border-bottom:1.5px solid #222;transform:rotate(45deg);margin-left:8px;position:relative;top:-3px}
.contact-btn{position:absolute;left:958px;top:26px;width:132px;height:36px;border:1.5px solid var(--blue);color:var(--blue);font-size:13px;font-weight:500;display:flex;align-items:center;justify-content:center}

/* hero */
.hero{position:absolute;left:0;top:86px;width:1200px;height:609px;background:linear-gradient(90deg,#f6f7f8 0%,#eef0f2 45%,#e4e6e8 100%)}
.hero-photo{position:absolute;left:505px;top:86px;width:695px;height:609px;background:linear-gradient(120deg,#d8dde2 0%,#bfc6cd 40%,#9aa3ad 70%,#c9b49a 100%)}
.hero-title{position:absolute;left:110px;top:182px;font-size:54px}
.hero-lead{position:absolute;left:110px;top:304px;width:400px;font-size:12.5px;line-height:1.45;color:#222}
.point{position:absolute;width:205px;font-family:"Roboto Condensed",sans-serif;font-weight:700;font-size:10.5px;line-height:1.45;color:#222;text-transform:uppercase;padding-left:17px}
.point::before{content:"";position:absolute;left:0;top:3px;border-left:7px solid var(--yellow);border-top:4.5px solid transparent;border-bottom:4.5px solid transparent}
.hero-tag{position:absolute;left:110px;top:495px;font-size:12.5px;color:#222}

/* services */
.section-title{position:absolute;left:0;width:1200px;text-align:center;font-size:44px}
.intro{position:absolute;left:249px;top:904px;width:702px;text-align:center;font-size:12.5px;line-height:1.4;color:#222}
.svc{position:absolute;width:300px;height:300px;border:1px solid var(--line);background:var(--card);font-family:"Montserrat",sans-serif}
.svc .icon{position:absolute;left:30px;top:40px;width:72px;height:72px}
.svc h3{position:absolute;left:30px;top:138px;font-size:20px;font-weight:700;line-height:1.25;color:#111}
.svc p{position:absolute;left:30px;top:206px;width:245px;font-size:13px;line-height:1.5;color:#333}
.svc.active{background:var(--blue);border-color:var(--blue);box-shadow:0 10px 24px rgba(0,0,0,.18)}
.svc.active h3,.svc.active p{color:#fff}
.svc.intro-card{background:#fff}
.svc.intro-card h3{left:0;width:300px;text-align:center;top:55px;font-size:26px;font-weight:500}
.svc.intro-card h3 b{font-weight:700}
.caption{position:absolute;left:0;top:1726px;width:1200px;text-align:center;font-size:12px;color:#222}

/* people */
.people-band{position:absolute;left:100px;top:2060px;width:272px;height:264px;background:var(--blue)}
.people-photo{position:absolute;left:110px;top:1841px;width:515px;height:473px;background:linear-gradient(160deg,#5f6a73 0%,#a9b4bd 35%,#d8dee3 60%,#7d8790 100%)}
.people-card{position:absolute;left:537px;top:1910px;width:553px;height:487px;background:#fff;box-shadow:0 4px 22px rgba(0,0,0,.12)}
.people-card h2{position:absolute;left:74px;top:76px;font-size:44px}
.people-card .body{position:absolute;left:74px;width:410px;font-size:12px;line-height:1.45;color:#222}
.people-card .point{width:400px;left:74px}

/* testimonials */
.testimonials{position:absolute;left:0;top:2498px;width:1200px;height:521px;background:var(--band)}
.quote-card{position:absolute;text-align:center;font-family:"Montserrat",sans-serif}
.quote-card .mark{font-family:"Roboto Condensed",sans-serif;font-weight:700;color:var(--yellow);line-height:1}
.quote-card.side{width:263px;height:183px;top:2675px;background:#fff;opacity:.55;padding:20px 30px}
.quote-card.side .mark{font-size:52px}
.quote-card.side p{font-size:8px;line-height:1.5;color:#999}
.quote-card.side .who{font-size:6.5px;color:#aaa;margin-top:10px;text-transform:uppercase}
.quote-card.main{left:411px;top:2646px;width:379px;height:241px;background:var(--blue);color:#fff;padding:24px 30px}
.quote-card.main .mark{font-size:72px;height:56px}
.quote-card.main p{font-size:11.5px;line-height:1.5;margin-top:8px}
.quote-card.main .who{font-size:10px;font-weight:700;margin-top:8px;text-transform:uppercase}
.quote-card.main .org{font-size:9.5px;margin-top:4px}
.stars{color:var(--yellow);letter-spacing:2px;font-size:12px;margin-top:4px}
.arrow{position:absolute;top:2753px;width:30px;height:30px;border:1px solid #555;background:#fff;display:flex;align-items:center;justify-content:center}
.dot{position:absolute;width:9px;height:9px;border-radius:50%}

/* technologies */
.tech{position:absolute;top:3184px;width:180px;height:81px;border:1px solid var(--line);display:flex;align-items:center;justify-content:center;font-family:"Montserrat",sans-serif;font-weight:600;font-size:19px;color:#333}

/* footer */
.site-footer{position:absolute;left:0;top:3391px;width:1200px;height:378px;background:var(--footer);color:#ddd}
.footer-brand{position:absolute;left:100px;top:84px;font-size:46px;color:#e9e9e9;letter-spacing:-1px}
.social{position:absolute;top:150px;width:36px;height:36px;border:1px solid #555}
.f-col{position:absolute;top:85px;font-family:"Montserrat",sans-serif}
.f-col h4{font-size:14px;font-weight:700;color:#fff;margin-bottom:18px}
.f-col li{list-style:none;font-size:12.5px;line-height:23px;color:#ddd}
.contact-row{position:absolute;left:859px;display:flex;gap:12px;font-family:"Montserrat",sans-serif;font-size:12.5px;line-height:1.45;color:#eee}
.footer-rule{position:absolute;left:110px;top:282px;width:980px;height:3px;background:#444}
.copyright{position:absolute;left:0;top:310px;width:1200px;text-align:center;font-size:11px;color:#ddd}
</style>
</head>
<body>

<header class="site-header">
  <div class="brand">Norvalith</div>
  <div class="nav-item" style="left:527px">About Us</div>
  <div class="nav-item" style="left:642px">Services</div>
  <div class="nav-item" style="left:757px">Insights</div>
  <div class="nav-item" style="left:866px">Join Us</div>
  <div class="contact-btn">Contact Us</div>
</header>

<section class="hero" aria-label="Hero"></section>
<div class="hero-photo" role="img" aria-label="Photo of two colleagues working together at a laptop in a bright office"></div>
<div class="sq" style="left:706px;top:340px;width:36px;height:36px;background:var(--blue)"></div>
<div class="sq" style="left:710px;top:395px;width:24px;height:24px;background:var(--yellow)"></div>
<div class="sq" style="left:670px;top:418px;width:24px;height:24px;background:#a7b4ec"></div>
<div class="sq" style="left:806px;top:276px;width:30px;height:42px;background:var(--blue)"></div>
<div class="sq" style="left:946px;top:306px;width:36px;height:36px;background:var(--yellow)"></div>
<div class="sq" style="left:553px;top:195px;width:18px;height:18px;background:#aab5c2"></div>
<div class="sq" style="left:5px;top:354px;width:14px;height:14px;background:var(--yellow);transform:rotate(20deg)"></div>

<h1 class="heading hero-title">Transformation<br><span class="accent">Delivered.</span></h1>
<p class="hero-lead">The world has changed in the past twenty years. The people you need might not all work for one company.</p>
<div class="point" style="left:110px;top:364px">Focus on business value, with an emphasis on delivering value quickly.</div>
<div class="point" style="left:380px;top:364px">Provide a wide range of services, from strategy to product support.</div>
<div class="point" style="left:110px;top:428px">Meet our customers where they are without backing them up to the beginning of their journey.</div>
<div class="point" style="left:380px;top:428px">Commit to our customer's long-term success.</div>
<p class="hero-tag">Norvalith is business transformation, delivered.</p>
<div class="btn" style="left:110px;top:534px;width:153px;height:44px">Our Story</div>
<div class="sq" style="left:306px;top:651px;width:13px;height:13px;background:var(--yellow)"></div>
<div class="sq" style="left:273px;top:674px;width:29px;height:29px;background:var(--blue)"></div>

<!-- services -->
<h2 class="heading section-title" style="top:792px">Transformation<br><span class="accent">Supported By Technology</span></h2>
<div class="sq" style="left:1068px;top:867px;width:22px;height:22px;background:var(--sky)"></div>
<p class="intro">During our early years, Norvalith focused only on business transformation. We came to realize that successful transformation often depended on quality software implementations, and often more than one. Now we focus on five things, the five things most businesses need to reach their goals.</p>

<div class="svc intro-card" style="left:110px;top:992px">
  <h3><b>How</b> We Work</h3>
  <svg class="abs" style="left:160px;top:175px" width="140" height="125" viewBox="0 0 140 125">
    <rect x="110" y="0" width="30" height="30" fill="none" stroke="#c9d3e4" stroke-width="4"/>
    <rect x="83" y="42" width="26" height="26" fill="#c4d0e6"/>
    <rect x="40" y="60" width="26" height="26" fill="#c4d0e6"/>
    <rect x="125" y="70" width="15" height="15" fill="#dfe3f5"/>
    <rect x="80" y="95" width="26" height="26" fill="#dfe0f8"/>
    <rect x="42" y="100" width="18" height="18" fill="#f1e6ad"/>
    <rect x="15" y="112" width="13" height="13" fill="#dfe0f8"/>
    <rect x="122" y="107" width="18" height="18" fill="#f5eebf"/>
  </svg>
</div>

<div class="svc" style="left:449px;top:992px">
  <svg class="icon" viewBox="0 0 72 72" role="img" aria-label="Strategy chart icon"><ellipse cx="30" cy="38" rx="28" ry="30" fill="#f3e39b"/><rect x="20" y="22" width="34" height="26" fill="none" stroke="#222" stroke-width="2"/><path d="M26 42v-6M32 42v-10M38 42v-14M44 42v-8" stroke="#222" stroke-width="3"/></svg>
  <h3>Business<br>Transformation</h3>
  <p>Define and execute your strategy.</p>
</div>

<div class="svc active" style="left:790px;top:992px">
  <svg class="icon" viewBox="0 0 72 72" role="img" aria-label="ERP gear icon"><ellipse cx="30" cy="38" rx="28" ry="24" fill="#3a74aa"/><circle cx="40" cy="40" r="16" fill="none" stroke="#fff" stroke-width="2"/><circle cx="40" cy="40" r="9" fill="none" stroke="#fff" stroke-width="1.5"/><text x="40" y="43" font-size="8" fill="#fff" text-anchor="middle" font-family="Montserrat,sans-serif">ERP</text></svg>
  <h3>ERP<br>Implementations</h3>
  <p>Assess, upgrade, and implement ERP solutions to meet your needs.</p>
</div>

<div class="svc" style="left:110px;top:1330px">
  <svg class="icon" viewBox="0 0 72 72" role="img" aria-label="CRM screen icon"><ellipse cx="26" cy="36" rx="24" ry="30" fill="#f3e39b"/><rect x="18" y="18" width="42" height="32" fill="#fff" stroke="#222" stroke-width="2"/><text x="42" y="30" font-size="8" fill="#222" font-family="Montserrat,sans-serif" font-weight="700">CRM</text><path d="M30 42l6-5 5 3 8-7" stroke="#222" stroke-width="2" fill="none"/></svg>
  <h3>CRM<br>Implementations</h3>
  <p>Take your relationships to the next level.</p>
</div>

<div class="svc" style="left:449px;top:1330px">
  <svg class="icon" viewBox="0 0 72 72" role="img" aria-label="Data dashboard icon"><ellipse cx="34" cy="34" rx="32" ry="24" fill="#f3e39b"/><rect x="20" y="16" width="36" height="28" fill="#fff" stroke="#222" stroke-width="2"/><path d="M28 38v-6M34 38v-10M40 38v-8M46 38v-14" stroke="#222" stroke-width="3"/><path d="M34 44v8M26 52h16" stroke="#222" stroke-width="2"/></svg>
  <h3>BI and Data</h3>
  <p>Discover, connect, and trust your data.</p>
</div>

<div class="svc" style="left:790px;top:1330px">
  <svg class="icon" viewBox="0 0 72 72" role="img" aria-label="Team gear icon"><circle cx="30" cy="34" r="30" fill="#f3e39b"/><circle cx="42" cy="38" r="16" fill="none" stroke="#222" stroke-width="2" stroke-dasharray="5 3"/><circle cx="42" cy="34" r="4" fill="#222"/><path d="M34 46c2-6 14-6 16 0" stroke="#222" stroke-width="2" fill="none"/></svg>
  <h3>Building the<br>Right Team of People</h3>
  <p>Hire resources for your transformation journey.</p>
</div>

<div class="btn" style="left:520px;top:1662px;width:160px;height:44px">How We Work</div>
<p class="caption">Find Out How Norvalith Can Help You Put All The Pieces Together And Get Them Done.</p>

<!-- people -->
<div class="sq" style="left:25px;top:1800px;width:28px;height:28px;background:var(--sky)"></div>
<div class="people-band"></div>
<div class="people-photo" role="img" aria-label="Photo of a consultant presenting charts to a team in a glass-walled meeting room"></div>
<div class="people-card">
  <h2 class="heading">It's The <span class="accent">People</span></h2>
  <p class="body" style="top:130px">The world has changed in the past twenty years. The people you need might not all work for one company. Our clients want the best resources, available quickly. That's why, in addition to our team of experts, we partner with:</p>
  <div class="point" style="top:217px">A large network of expert consultants who are the best at what they do,</div>
  <div class="point" style="top:262px">Service providers all over the world to provide the resources and value that are right for you, available 24 x 7.</div>
  <p class="body" style="top:316px">People are invariably at the center of our customer's success. Find out how we can add our experts to yours.</p>
  <div class="btn" style="left:75px;top:376px;width:167px;height:42px">Meet Our Team</div>
</div>
<div class="sq" style="left:1163px;top:2466px;width:13px;height:13px;background:var(--yellow)"></div>

<!-- testimonials -->
<section class="testimonials"></section>
<h2 class="heading section-title" style="top:2574px">Our <span class="accent">Testimonials</span></h2>
<div class="quote-card side" style="left:176px">
  <div class="mark">&ldquo;</div>
  <p>Norvalith created a sensible and actionable roadmap to incrementally address the greatest priorities and lowest hanging fruit – and then worked with us to put these improvements into action.</p>
  <div class="who">Dana Whitfield, Chief Operating Officer<br>Brightwell Clinics</div>
  <div class="stars" style="font-size:8px">★★★★★</div>
</div>
<div class="quote-card side" style="left:761px">
  <div class="mark">&ldquo;</div>
  <p>Norvalith created a sensible and actionable roadmap to incrementally address the greatest priorities and lowest hanging fruit – and then worked with us to put these improvements into action.</p>
  <div class="who">Dana Whitfield, Chief Operating Officer<br>Brightwell Clinics</div>
  <div class="stars" style="font-size:8px">★★★★★</div>
</div>
<div class="quote-card main">
  <div class="mark">&ldquo;</div>
  <p>Norvalith created a sensible and actionable roadmap to incrementally address the greatest priorities and lowest hanging fruit – and then worked with us to put these improvements into action.</p>
  <div class="who">Dana Whitfield, Chief Operating Officer</div>
  <div class="org">Brightwell Clinics</div>
  <div class="stars">★★★★★</div>
</div>
<div class="arrow" style="left:110px"><svg width="10" height="12" viewBox="0 0 10 12"><path d="M7 1L2 6l5 5" stroke="#333" stroke-width="1.5" fill="none"/></svg></div>
<div class="arrow" style="left:1060px"><svg width="10" height="12" viewBox="0 0 10 12"><path d="M3 1l5 5-5 5" stroke="#333" stroke-width="1.5" fill="none"/></svg></div>
<div class="dot" style="left:570px;top:2923px;background:var(--blue)"></div>
<div class="dot" style="left:588px;top:2923px;background:#aab"></div>
<div class="dot" style="left:606px;top:2923px;background:#aab"></div>
<div class="dot" style="left:623px;top:2923px;background:#aab"></div>
<div class="sq" style="left:128px;top:3018px;width:24px;height:22px;background:var(--sky)"></div>

<!-- technologies -->
<h2 class="heading section-title" style="top:3105px">Techno<span class="accent">logies</span></h2>
<div class="tech" style="left:110px">Quorra</div>
<div class="tech" style="left:310px">Ledgerline</div>
<div class="tech" style="left:510px">Vantora Suite</div>
<div class="tech" style="left:710px">Datavane</div>
<div class="tech" style="left:910px">Orbis Cloud</div>
<div class="dot" style="left:568px;top:3298px;border:1.5px solid #889"></div>
<div class="dot" style="left:586px;top:3298px;background:var(--yellow)"></div>
<div class="dot" style="left:604px;top:3298px;border:1.5px solid #889"></div>
<div class="dot" style="left:622px;top:3298px;border:1.5px solid #889"></div>

<!-- footer -->
<footer class="site-footer">
  <div class="footer-brand">Norvalith</div>
  <div class="social" style="left:127px" aria-label="Social link"></div>
  <div class="social" style="left:173px;background:var(--blue);border-color:var(--blue)" aria-label="Social link"></div>
  <div class="social" style="left:219px" aria-label="Social link"></div>
  <div class="social" style="left:267px" aria-label="Social link"></div>

  <div class="f-col" style="left:439px"><h4>Quick Links</h4><ul><li>About Us</li><li>Services</li><li>Insights</li><li>Join Us</li></ul></div>
  <div class="f-col" style="left:648px"><h4>More Links</h4><ul><li>Privacy Policy</li><li>Terms And</li><li>Conditions</li><li>Sitemap</li></ul></div>
  <div class="f-col" style="left:859px"><h4>Contact Us</h4></div>

  <div class="contact-row" style="top:120px">
    <svg width="16" height="18" viewBox="0 0 16 18"><path d="M8 17s6-6 6-10A6 6 0 0 0 2 7c0 4 6 10 6 10z" fill="none" stroke="#6a9bd0" stroke-width="1.4"/><circle cx="8" cy="7" r="2" fill="none" stroke="#6a9bd0" stroke-width="1.4"/></svg>
    <span>48 Larkspur Avenue<br>Suite 210, Fairmont, MN 55901</span>
  </div>
  <div class="contact-row" style="top:170px;font-weight:700;letter-spacing:1px">
    <svg width="16" height="16" viewBox="0 0 16 16"><path d="M3 1l3 3-2 2c1 2 3 4 5 5l2-2 3 3-2 3C7 15 1 9 1 3z" fill="none" stroke="#6a9bd0" stroke-width="1.3"/></svg>
    <span>(555) 018-2740</span>
  </div>
  <div class="contact-row" style="top:203px">
    <svg width="16" height="14" viewBox="0 0 16 14"><rect x="1" y="2" width="14" height="10" fill="none" stroke="#6a9bd0" stroke-width="1.3"/><path d="M1 2l7 6 7-6" fill="none" stroke="#6a9bd0" stroke-width="1.3"/></svg>
    <span style="color:var(--yellow);text-decoration:underline">info@norvalithconsulting.example</span>
  </div>

  <div class="footer-rule"></div>
  <p class="copyright">©2023 Norvalith Consulting. All Rights Reserved.</p>
</footer>

</body>
</html>
```